Poster Design for kebab shop products

need a new poster for our new blazer tray special, sign will be inside of shopping centre at different location to shop will need to stand out and draw customers to the store, MUST contain shops logo & picture added, poster size will be 76cm x 101cm so will need to suit that size

MUST ALSO CONTAIN THE FOLLOWING
Blazer Tray / HSP
Lamb & Chips
Chicken & Chips
Beef & Chips
+ Can $15

Target Market(s)

new customers

Industry/Entity Type

Retail

Font styles to use
Sans Serif

Colors

Designer to choose colors to be used in the design.

Requirements
Must have
• company logo
• picture of blazr tray provided
• Blazer Tray / HSP
• Lamb & Chips
• Chicken & Chips
• Beef & Chips
• + Can $15

```html
<!DOCTYPE html>
<html lang="en">
<head>
<meta charset="utf-8">
<title>Shawarma Cove – Blazer Tray Special</title>
<link rel="stylesheet" href="https://fonts.googleapis.com/css2?family=Bebas+Neue&family=Oswald:wght@700&family=Alfa+Slab+One&family=Archivo+Black&display=swap">
<style>
  :root {
    --red-deep: #4a070b;
    --red-mid: #8e1016;
    --red-bright: #d3161e;
    --wine: #2a0406;
    --white: #ffffff;
    --silver: #d9d9d9;
    --yellow: #e2b814;
    --beef-red: #e3141b;
    --orange: #f39a1e;
    --black-band: #1a1a1a;
  }
  * { margin: 0; padding: 0; box-sizing: border-box; }
  html, body { width: 950px; height: 1200px; overflow: hidden; background: #eeeeee; }
  .poster {
    position: relative;
    width: 950px;
    height: 1200px;
    overflow: hidden;
    background: radial-gradient(ellipse at 50% 30%, var(--red-mid) 0%, var(--red-deep) 60%, var(--wine) 100%);
  }
  .poster__lower {
    position: absolute; left: 0; right: 0; bottom: 0; height: 380px;
    background: linear-gradient(180deg, #3d0609 0%, var(--wine) 100%);
  }
  .poster__art { position: absolute; inset: 0; }
  .brand-plaque {
    position: absolute; left: 204px; top: 0; width: 539px; height: 220px;
    display: flex; align-items: center; justify-content: center; gap: 14px;
  }
  .brand-plaque__dot { width: 34px; height: 34px; border-radius: 50%; background: var(--orange); }
  .brand-plaque__name {
    font-family: "Bebas Neue", sans-serif;
    font-size: 64px; line-height: 1; color: var(--red-bright); letter-spacing: 1px;
  }
  .offer__line {
    position: absolute; left: 52px;
    display: block; white-space: nowrap; line-height: 1;
  }
  .offer__title {
    top: 850px;
    font-family: "Bebas Neue", sans-serif; font-size: 92px; color: var(--white);
  }
  .offer__lamb {
    top: 932px;
    font-family: "Oswald", sans-serif; font-weight: 700; font-size: 66px;
    color: var(--yellow); letter-spacing: 1px;
  }
  .offer__chicken {
    top: 1008px;
    font-family: "Alfa Slab One", serif; font-size: 52px; color: var(--white);
  }
  .offer__beef {
    top: 1066px;
    font-family: "Bebas Neue", sans-serif; font-size: 90px; color: var(--beef-red);
  }
  .offer__can { color: var(--silver); }
  .price-tag__amount {
    position: absolute; left: 603px; top: 920px; width: 300px;
    text-align: center; line-height: 1.2;
    font-family: "Archivo Black", sans-serif; font-size: 112px; color: var(--white);
    letter-spacing: -4px;
    text-shadow: 0 4px 0 #8a8a8a, 0 8px 12px rgba(0,0,0,.5);
  }
</style>
</head>
<body>
<main class="poster">
  <div class="poster__lower"></div>

  <svg class="poster__art" width="950" height="1200" viewBox="0 0 950 1200" xmlns="http://www.w3.org/2000/svg">
    <defs>
      <linearGradient id="trayFill" x1="0" y1="0" x2="0" y2="1">
        <stop offset="0" stop-color="#f0d470"/>
        <stop offset=".45" stop-color="#8a5530"/>
        <stop offset="1" stop-color="#e8c55a"/>
      </linearGradient>
      <radialGradient id="tagFill" cx=".4" cy=".35" r=".7">
        <stop offset="0" stop-color="#e2262b"/>
        <stop offset="1" stop-color="#8a0a0e"/>
      </radialGradient>
      <clipPath id="photoClip"><circle cx="472" cy="455" r="334"/></clipPath>
    </defs>

    <!-- side swoosh bands, kept above the offer heading -->
    <path class="swoosh swoosh--black" d="M0 480 Q170 780 472 800 Q775 780 950 480 L950 580 Q775 820 472 820 Q170 820 0 580 Z" fill="var(--black-band)"/>
    <path class="swoosh swoosh--red" d="M0 560 Q170 810 472 820 Q775 810 950 560 L950 640 Q775 838 472 838 Q170 838 0 640 Z" fill="var(--red-bright)"/>
    <path class="swoosh swoosh--white" d="M0 640 Q170 835 472 838 Q775 835 950 640 L950 665 Q775 848 472 848 Q170 848 0 665 Z" fill="#f2f2f2"/>

    <!-- photo frame rings -->
    <circle cx="472" cy="455" r="368" fill="#f4f4f4"/>
    <circle cx="472" cy="455" r="354" fill="none" stroke="var(--red-bright)" stroke-width="6"/>
    <circle cx="472" cy="455" r="344" fill="#ffffff"/>

    <g role="img" aria-label="Photo of a blazer tray: sliced kebab meat over hot chips, drizzled with garlic and chilli sauce">
      <rect x="130" y="110" width="690" height="690" fill="url(#trayFill)" clip-path="url(#photoClip)"/>
    </g>

    <!-- logo plaque frame -->
    <path class="brand-plaque__frame" d="M232 0 L715 0 L715 40 Q740 44 743 70 L743 200 Q716 206 708 232 Q610 236 566 220 Q505 210 473 262 Q441 210 380 220 Q336 236 238 232 Q230 206 204 200 L204 70 Q208 44 232 40 Z" fill="var(--red-bright)"/>
    <path d="M244 0 L703 0 L703 50 Q726 56 729 78 L729 192 Q706 198 698 220 Q610 222 562 208 Q503 200 473 240 Q443 200 384 208 Q336 222 248 220 Q240 198 218 192 L218 78 Q222 56 244 50 Z" fill="var(--white)"/>

    <!-- price tag -->
    <path class="price-tag__string" d="M753 865 Q790 770 900 740" fill="none" stroke="#6b4a33" stroke-width="2"/>
    <circle cx="753" cy="990" r="150" fill="#cfcfcf"/>
    <circle cx="753" cy="990" r="140" fill="url(#tagFill)"/>
    <circle cx="753" cy="868" r="14" fill="#e6e6e6" stroke="#888" stroke-width="3"/>
  </svg>

  <header class="brand-plaque">
    <span class="brand-plaque__dot"></span>
    <span class="brand-plaque__name">Shawarma Cove</span>
  </header>

  <section class="offer">
    <span class="offer__line offer__title">BLAZER TRAY / HSP</span>
    <span class="offer__line offer__lamb">LAMB &amp; CHIPS</span>
    <span class="offer__line offer__chicken">CHICKEN &amp; CHIPS</span>
    <span class="offer__line offer__beef">BEEF &amp; CHIPS <span class="offer__can">+ CAN</span></span>
  </section>

  <div class="price-tag__amount">$15</div>
</main>
</body>
</html>
```